Business card design needed

Chasing a very simplistic modern design with a logo incorporating "TRV".
I'm starting a plumbing business.
I do water, sanitary and drainage plumbing that will cover residential, commercial, rental, rural, excavation, new housing and all maintanence requirements.

Industry/Entity Type

Business

Contact Information for Business Card

TRV PLUMBING SERVICES
DEAN HOLLOWBY - LICENSED PLUMBER
PHONE: 0481926574
E-MAIL: hollodt7@wirelane.com
NORTHERN SUBURBS

Requirements
Must have
• lower case email address

```html
<!DOCTYPE html>
<html lang="en">
<head>
<meta charset="utf-8">
<title>TRV Plumbing Services – Business Cards</title>
<link rel="stylesheet" href="https://fonts.googleapis.com/css2?family=Questrial&display=swap">
<style>
  :root {
    --bg: #d9d9d9;
    --card: #050505;
    --card-low: #141414;
    --swoosh: #5a5a5a;
    --swoosh-soft: #2c2c2c;
    --white: #ffffff;
    --text-light: #e6e6e6;
    --blue: #4aa3e0;
    --logo-blue: #8ea7cf;
    --logo-dark: #111111;
    --logo-grey: #6b6b6b;
  }
  * { margin: 0; padding: 0; box-sizing: border-box; }
  html, body { width: 1200px; height: 1059px; overflow: hidden; }
  body {
    background: var(--bg);
    font-family: "Questrial", "Helvetica Neue", Arial, sans-serif;
    position: relative;
  }
  .card {
    position: absolute;
    left: 48px;
    width: 741px;
    height: 458px;
    background: var(--card);
    overflow: hidden;
  }
  .card--front { top: 49px; }
  .card--back { top: 538px; }
  .card__swoosh { position: absolute; inset: 0; width: 100%; height: 100%; }

  .brand-name {
    display: block;
    font-weight: 400;
    color: var(--logo-blue);
    letter-spacing: 0.02em;
    line-height: 1;
  }
  .brand-tag {
    display: block;
    color: var(--text-light);
    letter-spacing: 0.2em;
    line-height: 1;
  }

  .front-brand {
    position: absolute;
    left: 0; right: 0;
    top: 118px;
    text-align: center;
  }
  .front-brand .brand-name { font-size: 104px; }
  .front-brand .brand-tag { font-size: 22px; margin-top: 18px; }

  .back-brand {
    position: absolute;
    left: 38px;
    top: 20px;
  }
  .back-brand .brand-name { font-size: 82px; }
  .back-brand .brand-tag { font-size: 18px; margin-top: 10px; }

  .services {
    position: absolute;
    left: 30px;
    top: 128px;
    width: 620px;
    font-size: 13px;
    line-height: 19px;
    color: var(--text-light);
    text-transform: uppercase;
    letter-spacing: 0.02em;
  }

  .person {
    position: absolute;
    right: 56px;
    top: 204px;
    text-align: right;
  }
  .person__name {
    font-size: 38px;
    line-height: 1;
    color: var(--white);
    letter-spacing: -0.01em;
  }
  .person__name .surname { color: var(--blue); }
  .person__role {
    font-size: 12px;
    letter-spacing: 0.18em;
    color: var(--text-light);
    margin-top: 6px;
  }

  .contact {
    position: absolute;
    left: 56px;
    top: 280px;
    list-style: none;
  }
  .contact__item {
    display: flex;
    align-items: center;
    gap: 14px;
    font-size: 23px;
    color: var(--white);
    height: 34px;
  }
  .contact__icon { width: 22px; height: 22px; flex: none; }

  .brand-display {
    position: absolute;
    left: 847px;
    top: 858px;
    width: 320px;
    text-align: center;
  }
  .brand-display .brand-name { font-size: 92px; color: var(--logo-dark); }
  .brand-display .brand-tag { font-size: 21px; color: var(--logo-grey); margin-top: 10px; letter-spacing: 0.16em; }
</style>
</head>
<body>

<section class="card card--front" aria-label="Business card front">
  <svg class="card__swoosh" viewBox="0 0 741 458" preserveAspectRatio="none" aria-hidden="true">
    <path d="M0 330 Q300 400 741 262 L741 458 L0 458 Z" fill="var(--card-low)"/>
    <path d="M0 330 Q300 400 741 262 L741 280 Q300 410 0 342 Z" fill="var(--swoosh)"/>
    <path d="M0 360 Q280 410 741 300 L741 306 Q280 418 0 368 Z" fill="var(--swoosh-soft)"/>
  </svg>
  <div class="front-brand">
    <span class="brand-name">TRV</span>
    <span class="brand-tag">PLUMBING SERVICES</span>
  </div>
</section>

<section class="card card--back" aria-label="Business card back">
  <svg class="card__swoosh" viewBox="0 0 741 458" preserveAspectRatio="none" aria-hidden="true">
    <path d="M0 372 Q300 430 741 286 L741 458 L0 458 Z" fill="var(--card-low)"/>
    <path d="M0 372 Q300 430 741 286 L741 302 Q300 440 0 384 Z" fill="var(--swoosh)"/>
    <path d="M0 400 Q280 440 741 322 L741 328 Q280 448 0 408 Z" fill="var(--swoosh-soft)"/>
  </svg>
  <div class="back-brand">
    <span class="brand-name">TRV</span>
    <span class="brand-tag">PLUMBING SERVICES</span>
  </div>
  <p class="services">Water, sanitary and drainage plumbing for domestic, commercial, new housing, rental, rural and maintanence</p>
  <div class="person">
    <div class="person__name">DEAN<span class="surname">HOLLOWBY</span></div>
    <div class="person__role">LICENSED PLUMBER</div>
  </div>
  <ul class="contact">
    <li class="contact__item">
      <svg class="contact__icon" viewBox="0 0 22 22" aria-hidden="true">
        <rect x="6" y="3" width="10" height="17" rx="2" fill="var(--blue)"/>
        <rect x="8" y="5" width="6" height="6" fill="var(--card)"/>
        <rect x="13" y="0" width="2" height="4" fill="var(--blue)"/>
      </svg>
      04 819 265 74
    </li>
    <li class="contact__item">
      <svg class="contact__icon" viewBox="0 0 22 22" aria-hidden="true">
        <rect x="2" y="5" width="18" height="12" fill="var(--blue)"/>
        <path d="M2 5 L11 12 L20 5" fill="none" stroke="var(--card)" stroke-width="1.5"/>
      </svg>
      hollodt7@wirelane.com
    </li>
  </ul>
</section>

<div class="brand-display" aria-label="TRV Plumbing Services brand">
  <span class="brand-name">TRV</span>
  <span class="brand-tag">PLUMBING SERVICES</span>
</div>

</body>
</html>
```